Header/Logo Redesign

****WE HAVE FOUND THE DESIGNER WHO WILL BE HANDLING THIS PROJECT. PLEASE DONT SUBMIT ANY MORE DESIGNS.****
We have been working with a Web/Logo Designer on a new header and logo for our site. We like some of it, but other things need changing.
Overall Look: We are looking for something that is professional, yet still fresh. Most business two business websites seem old fashinoned. The site we like most is www.tallyhaven.com.
Header Thoughts:
-We like the color at the top of the header. The light purple on the menu bar is a little dull though. It seems to be grayed out too much. Notice the pop that www.tallyhaven.com has. We need that pop.
-The fonts on the menu bar don't pop either. I don't know if it is because the font is bad or the thickness of the font is bad or what.
-We are not sold on the green color in the logo and header. It is pretty good, but maybe we can test other colors?
Logo Thoughts:
-I am not sold on the green color. It is pretty good, but maybe test it out with some other colors?
-The logo does not pop like the www.tallyhaven.com logo pops.
-We had started thinking about doing an owl as part of our name/logo or maybe some other type of animal. Look at the ideas I had sent our original graphic designer.
A. http://markvista.net/gallery/detail/842907 - i like that is simple, a little abstract, but I don't like that it is sort of evil.
B. http://markvista.net/gallery/detail/27514 - i like that is abstract.
C. http://pixelbrook.files.quillsite.net/2012/05/torvane4.jpg - i like the slightly abstract.
D. http://sketchlark.net/shots/718204-O-W-L - good - abrstract and slightly turned.
Target Market(s)
Sales and Marketing People - primarily a masculine audience in their 20s to 40s.
Industry/Entity Type
Business
Look and feel

```html
<!DOCTYPE html>
<html lang="en">
<head>
<meta charset="utf-8">
<title>Scout902 — Header</title>
<link rel="stylesheet" href="https://fonts.googleapis.com/css2?family=Ubuntu:ital,wght@0,400;0,500;0,700;1,400&display=swap">
<style>
  :root {
    --header-top: #3f4069;
    --header-line: #2f3052;
    --menu-bar: #8382cb;
    --menu-bar-dark: #6f6eb6;
    --menu-divider: #4b4b7e;
    --menu-active: #f8f7f5;
    --menu-text: #ffffff;
    --menu-active-text: #1a1a1a;
    --panel: #4e4f80;
    --panel-inner: #8180c9;
    --tab-muted: #d9d8f2;
    --accent: #ffe600;
    --field: #ffffff;
    --placeholder: #777777;
  }
  * { box-sizing: border-box; margin: 0; padding: 0; }
  html, body { width: 1200px; height: 1000px; overflow: hidden; background: #fff; font-family: "Ubuntu", sans-serif; }
  .site-header { position: relative; width: 1200px; height: 116px; }
  .top-band { position: absolute; inset: 0 0 auto 0; height: 79px; background: var(--header-top); border-bottom: 1px solid var(--header-line); }
  .brand { position: absolute; left: 186px; top: 20px; display: flex; align-items: center; gap: 12px; }
  .brand-dot { width: 40px; height: 40px; border-radius: 50%; background: var(--accent); }
  .brand-name { color: #fff; font-weight: 700; font-size: 38px; letter-spacing: 0.5px; }
  .menu-bar { position: absolute; left: 0; right: 0; top: 79px; height: 37px;
    background: linear-gradient(var(--menu-bar-dark), var(--menu-bar) 25%, var(--menu-bar) 75%, var(--menu-bar-dark));
    border-bottom: 1px solid var(--menu-divider); }
  .main-nav { position: absolute; left: 194px; top: 0; height: 37px; display: flex; }
  .main-nav a { display: flex; align-items: center; justify-content: center; height: 37px; color: var(--menu-text);
    text-decoration: none; font-weight: 700; font-size: 17px; border-right: 1px solid var(--menu-divider); }
  .main-nav a.active { background: var(--menu-active); color: var(--menu-active-text); }
  .nav-new { width: 81px; } .nav-people { width: 90px; } .nav-companies { width: 119px; } .nav-downloads { width: 118px; }
  .search { position: absolute; left: 740px; top: 4px; width: 90px; height: 28px; border-radius: 14px 0 0 14px;
    background: var(--field); font-size: 14px; color: #333; padding: 6px 13px; }
  .login-panel { position: absolute; left: 809px; top: 0; width: 232px; height: 158px; background: var(--panel);
    border-radius: 0 0 22px 22px; }
  .tabs { position: absolute; left: 7px; top: 0; display: flex; height: 27px; }
  .tab { font-size: 14px; display: flex; align-items: center; justify-content: center; height: 27px; }
  .tab.current { width: 112px; background: var(--panel-inner); color: #fff; }
  .tab.other { width: 106px; color: var(--tab-muted); border-left: 1px solid var(--header-line); }
  .login-form { position: absolute; left: 7px; top: 27px; width: 219px; height: 104px; background: var(--panel-inner); }
  .field { position: absolute; left: 9px; width: 197px; height: 31px; background: var(--field);
    font-style: italic; font-size: 14px; color: var(--placeholder); padding: 7px 14px; }
  .field.user { top: 14px; } .field.pass { top: 59px; }
</style>
</head>
<body>
<header class="site-header">
  <div class="top-band">
    <div class="brand"><span class="brand-dot"></span><span class="brand-name">Scout902</span></div>
  </div>
  <div class="menu-bar">
    <nav class="main-nav">
      <a class="nav-new active" href="#">New</a>
      <a class="nav-people" href="#">People</a>
      <a class="nav-companies" href="#">Companies</a>
      <a class="nav-downloads" href="#">Downloads</a>
    </nav>
    <div class="search">search</div>
  </div>
  <div class="login-panel">
    <div class="tabs">
      <div class="tab current">Account Login</div>
      <div class="tab other">Free Sign Up</div>
    </div>
    <div class="login-form">
      <div class="field user">username</div>
      <div class="field pass">password</div>
    </div>
  </div>
</header>
</body>
</html>
```